QRSTREAMHUB ( Wordpress website for catalogue of Lumigram Live Pages)

Need a website to showcase different Lumigram Live pages ( in different categories). Similar to e-commerce except no check-out / purchase of items. Pls use our logos provided and color scheme to be white+red+ blue as per our logo.
Updates

Target Market(s)

Consumers

Font styles to use
Sans Serif

Colors
ffffff
ec1f27
3276b5

Requirements
Must have
• I will need a Wordpress Theme as a handover. Also, pls use the color scheme (red+blue+white) as per logo attached. Prefer clean and near design with white space.

```html
<!DOCTYPE html>
<html lang="en">
<head>
<meta charset="utf-8">
<title>QRSTREAMHUB – A Portal of Curated Lumigram Live</title>
<link rel="stylesheet" href="https://fonts.googleapis.com/css2?family=Roboto+Condensed:wght@300;400;700&display=swap">
<style>
:root{
  --blue:#1559d6;
  --red:#ee2747;
  --white:#ffffff;
  --ink:#1d1d1d;
  --grey-text:#5f5f5f;
  --panel:#f1f1f1;
  --line:#d6d6d6;
}
*{box-sizing:border-box;margin:0;padding:0}
html,body{width:1200px;height:3750px;overflow:hidden;background:var(--white);font-family:"Roboto Condensed",Arial,sans-serif;color:var(--ink)}
.page{position:relative;width:1200px;height:3750px}
.abs{position:absolute}

/* header */
.brand{left:132px;top:52px;font-size:31px;font-weight:700;color:var(--blue);letter-spacing:-0.5px;white-space:nowrap}
.nav{left:361px;top:51px;display:flex;align-items:center;height:36px}
.nav a{font-size:21px;color:#333;text-decoration:none;margin-right:40px;white-space:nowrap}
.nav a.active{background:var(--blue);color:var(--white);padding:0 15px;height:36px;line-height:36px;border-radius:3px;margin-right:25px}
.search{left:865px;top:52px;width:199px;height:35px;background:#f2f3f6;border-radius:4px;font-size:16px;color:#777;padding:9px 14px}
.search svg{position:absolute;right:10px;top:10px}

/* hero */
.hero-title{left:124px;top:222px;z-index:2;font-size:66px;font-weight:700;line-height:57px;letter-spacing:-2px;color:var(--ink);text-transform:uppercase;white-space:nowrap}
.hero-title .of{color:var(--red);font-size:50px;text-transform:none;letter-spacing:0}
.hero-live{display:inline-block;background:var(--red);color:var(--white);padding:4px 6px 0;line-height:52px;margin-top:6px;font-size:58px}
.hero-art{left:480px;top:167px;width:648px;height:313px;border-radius:140px 140px 20px 20px;background:linear-gradient(120deg,#e9eefb 0%,#cdd9f6 45%,#f7d6dc 100%)}
.band{height:9px;display:flex}
.band span:first-child{width:568px;background:var(--red)}
.band span:last-child{flex:1;background:var(--blue)}

/* sections */
.section-grey{background:var(--panel)}
.section-title{width:1200px;text-align:center;font-size:56px;font-weight:700;color:var(--blue);text-transform:uppercase;letter-spacing:-1px;white-space:nowrap}
.section-title .red{color:var(--red)}
.section-title .tag{display:inline-block;background:var(--red);color:var(--white);padding:0 12px;border-radius:4px;line-height:60px}

/* categories */
.cat{width:269px;height:210px;border-radius:4px}
.cat-label{position:absolute;left:28px;top:156px;width:215px;height:71px;background:var(--white);border-radius:4px;text-align:center;line-height:71px;font-size:20px;font-weight:700;color:#222;box-shadow:0 2px 6px rgba(0,0,0,.06)}

/* stream cards */
.card{width:265px;height:389px;background:var(--white);box-shadow:0 2px 10px rgba(0,0,0,.10);text-align:center}
.card-media{position:relative;height:165px}
.live-badge{position:absolute;right:12px;top:17px;font-size:18px;font-weight:700;color:var(--white);border:2px solid var(--red);background:rgba(238,39,71,.55);padding:0 3px;line-height:20px}
.card h3{font-size:20px;line-height:25px;color:var(--blue);font-weight:700;margin:38px 20px 8px}
.card p{font-size:17px;line-height:21px;color:var(--grey-text);font-weight:300;margin:0 24px}

/* about */
.about-photo{left:0;width:609px;height:543px;clip-path:polygon(0 0,609px 0,539px 543px,0 543px);background:radial-gradient(ellipse at 48% 50%,#f4c66a 0%,#b07a3b 28%,#4b3a2c 60%,#1e1a18 100%)}
.about-head{font-size:56px;font-weight:700;color:var(--blue);white-space:nowrap}
.about-head .tag{display:inline-block;background:var(--red);color:var(--white);padding:0 12px;border-radius:4px;line-height:60px}
.about-sub{font-size:29px;line-height:34px;color:var(--red);font-weight:700;width:400px}
.about-copy{font-size:17px;line-height:21.8px;color:var(--grey-text);font-weight:300;width:395px}
.btn{background:var(--red);color:var(--white);font-weight:700;font-size:20px;text-align:center;border-radius:4px}

/* contact */
.contact-intro{width:1200px;text-align:center;font-size:17px;line-height:22px;color:#777;font-weight:300}
.field{background:var(--white);border:1px solid var(--line);border-radius:3px;font-size:17px;color:#888;padding:12px 13px;font-weight:300}

/* footer */
.foot-links{left:170px;top:3658px;font-size:21px;color:#333}
.foot-links span{position:absolute;white-space:nowrap}
.copy{left:170px;top:3702px;font-size:13px;color:#333;white-space:nowrap}
.social{width:44px;height:40px;background:var(--red);border-radius:4px;top:3670px}
</style>
</head>
<body>
<div class="page">

  <!-- header -->
  <div class="abs brand">QRSTREAMHUB</div>
  <nav class="abs nav">
    <a class="active" href="#">Home</a>
    <a href="#">About Us</a>
    <a href="#">Stories</a>
    <a href="#">News</a>
    <a href="#">Conatct</a>
  </nav>
  <div class="abs search">Search
    <svg width="14" height="14" viewBox="0 0 14 14"><circle cx="5.5" cy="5.5" r="4" fill="none" stroke="#ee2747" stroke-width="2"/><line x1="8.5" y1="8.5" x2="13" y2="13" stroke="#ee2747" stroke-width="2.2"/></svg>
  </div>

  <!-- hero -->
  <div class="abs hero-art" role="img" aria-label="Illustration of a phone showing a live stream beside two shoppers carrying bags and boxes, with clothing, food and art items"></div>
  <h1 class="abs hero-title">A portal<span class="of">of</span><br>curated<br>Lumigram<br><span class="hero-live">Live</span></h1>
  <div class="abs band" style="left:0;top:504px;width:1200px"><span></span><span></span></div>

  <!-- categories -->
  <section class="abs section-grey" style="left:0;top:513px;width:1200px;height:696px"></section>
  <h2 class="abs section-title" style="left:0;top:554px">Categories</h2>
  <div class="abs cat" style="left:172px;top:635px;background:linear-gradient(135deg,#e9e6e3,#b7a59b)" role="img" aria-label="Woman browsing clothes in a boutique"><div class="cat-label">Loremsumor iam</div></div>
  <div class="abs cat" style="left:464px;top:635px;background:linear-gradient(135deg,#2b7fa0,#e0a24e)" role="img" aria-label="Hand painting a colourful canvas"><div class="cat-label">Loremsumor iam</div></div>
  <div class="abs cat" style="left:756px;top:635px;background:linear-gradient(160deg,#3b4a3c,#1f2a22)" role="img" aria-label="Football player kicking in a stadium"><div class="cat-label">Loremsumor iam</div></div>
  <div class="abs cat" style="left:172px;top:891px;background:linear-gradient(135deg,#d9a3a9,#8a6a70)" role="img" aria-label="Group of dancers performing"><div class="cat-label">Loremsumor iam</div></div>
  <div class="abs cat" style="left:464px;top:891px;background:linear-gradient(135deg,#d8d4cf,#4a4645)" role="img" aria-label="Cook stirring a pot on a stove"><div class="cat-label">Loremsumor iam</div></div>
  <div class="abs cat" style="left:756px;top:891px;background:radial-gradient(ellipse at 60% 30%,#f2d28c,#5a3a22 60%,#1b1412)" role="img" aria-label="Crowd at a concert under stage lights"><div class="cat-label">Loremsumor iam</div></div>

  <!-- featured -->
  <h2 class="abs section-title" style="left:0;top:1285px">Feature Lumigram <span class="tag">Live</span></h2>
  <svg class="abs" style="left:74px;top:1508px" width="36" height="78" viewBox="0 0 36 78"><polyline points="34,2 2,39 34,76" fill="none" stroke="#999" stroke-width="2"/></svg>
  <svg class="abs" style="left:1097px;top:1508px" width="36" height="78" viewBox="0 0 36 78"><polyline points="2,2 34,39 2,76" fill="none" stroke="#999" stroke-width="2"/></svg>

  <article class="abs card" style="left:172px;top:1395px">
    <div class="card-media" style="background:linear-gradient(180deg,#0c1410 0%,#1d3b22 55%,#3d7a35 100%)" role="img" aria-label="Floodlit empty football pitch"><span class="live-badge">LIVE</span></div>
    <h3>Lorem ipsum dolor sitam etconsectetur adipisc</h3>
    <p>Lorem ipsum dolor sit amet, consectetur adipiscing elit, sed do eiusmod tempor incididunt ut labore et dolore ma</p>
  </article>
  <article class="abs card" style="left:466px;top:1395px">
    <div class="card-media" style="background:linear-gradient(135deg,#cfcac3,#8f7a66)" role="img" aria-label="Woman cooking in a home kitchen"><span class="live-badge">LIVE</span></div>
    <h3>Lorem ipsum dolor sitam etonsectetur adipi</h3>
    <p>Lorem ipsum dolor sit amet, consectetur adipiscing elit, sed do eiusmod tempor incididunt ut labore et dolore ma</p>
  </article>
  <article class="abs card" style="left:760px;top:1395px">
    <div class="card-media" style="background:linear-gradient(135deg,#e8ebe2,#b9b59e)" role="img" aria-label="Woman chopping vegetables in a bright kitchen"><span class="live-badge">LIVE</span></div>
    <h3>Lorem ipsum dolor sitam etonsectetur adipi</h3>
    <p>Lorem ipsum dolor sit amet, consectetur adipiscing elit, sed do eiusmod tempor incididunt ut labore et dolore ma</p>
  </article>

  <!-- about -->
  <section class="abs section-grey" style="left:0;top:1903px;width:1200px;height:543px"></section>
  <div class="abs about-photo" style="top:1903px" role="img" aria-label="Concert crowd with raised hands facing a glowing stage"></div>
  <h2 class="abs about-head" style="left:655px;top:2000px">ABOUT <span class="tag">US</span></h2>
  <p class="abs about-sub" style="left:651px;top:2074px">Lorem ipsum dolor sitamet etur adipiscing elitsed do eiusmm</p>
  <p class="abs about-copy" style="left:651px;top:2155px">Sed ut perspiciatis unde omnis iste natus error sit volu usantium doloremque laudantium, totam rem aperiam, eaque ipsa quae ab illo inventore veritatis et quasi archi tecto beatae vitae dicta sunt explicabo. Nemo enim ips am voluptatem quia voluptas sit asp ernatur aut odit aut fugit, sed quia consequuntur magni dolores eos qui ratio ne voluptatem sequi nesciunt.</p>
  <div class="abs btn" style="left:651px;top:2317px;width:150px;height:52px;line-height:52px">READ MORE</div>

  <!-- now streaming -->
  <h2 class="abs section-title" style="left:0;top:2516px">Now <span class="red">Streaming</span></h2>
  <article class="abs card" style="left:172px;top:2625px">
    <div class="card-media" style="background:linear-gradient(180deg,#6a6f64 0%,#98a48c 50%,#4f8a35 100%)" role="img" aria-label="Football at a player's feet on grass"><span class="live-badge">LIVE</span></div>
    <h3>Lorem ipsum dolor sitam etconsectetur adipisc</h3>
    <p>Lorem ipsum dolor sit amet, consectetur adipiscing elit, sed do eiusmod tempor incididunt ut labore et dolore ma</p>
  </article>
  <article class="abs card" style="left:466px;top:2625px">
    <div class="card-media" style="background:linear-gradient(135deg,#3a1d6e,#2d63c8 50%,#b0317e)" role="img" aria-label="Phone filming a concert under blue and purple lights"><span class="live-badge">LIVE</span></div>
    <h3>Lorem ipsum dolor sitam etonsectetur adipi</h3>
    <p>Lorem ipsum dolor sit amet, consectetur adipiscing elit, sed do eiusmod tempor incididunt ut labore et dolore ma</p>
  </article>
  <article class="abs card" style="left:760px;top:2625px">
    <div class="card-media" style="background:linear-gradient(135deg,#5a3322,#b27a4b 55%,#2a1a14)" role="img" aria-label="Musician playing acoustic guitar into a microphone"><span class="live-badge">LIVE</span></div>
    <h3>Lorem ipsum dolor sitam etonsectetur adipi</h3>
    <p>Lorem ipsum dolor sit amet, consectetur adipiscing elit, sed do eiusmod tempor incididunt ut labore et dolore ma</p>
  </article>

  <!-- contact -->
  <section class="abs section-grey" style="left:0;top:3116px;width:1200px;height:507px"></section>
  <h2 class="abs section-title" style="left:0;top:3170px">Contact <span class="tag">Us</span></h2>
  <p class="abs contact-intro" style="left:0;top:3240px">usantium doloremque laudantium, totam rem aperiam, eaque ipsa quae ab illo inventore<br>veritatis et quasi architecto beatae vitae dicta sunt explicao enim ipsam voluptatem</p>
  <div class="abs field" style="left:218px;top:3318px;width:340px;height:47px">Name</div>
  <div class="abs field" style="left:218px;top:3380px;width:340px;height:46px">Email</div>
  <div class="abs field" style="left:218px;top:3439px;width:340px;height:47px">Phone</div>
  <div class="abs field" style="left:218px;top:3497px;width:340px;height:47px">Subject</div>
  <div class="abs field" style="left:566px;top:3318px;width:426px;height:166px">Message</div>
  <div class="abs btn" style="left:566px;top:3499px;width:424px;height:46px;line-height:46px">SUBMIT</div>

  <!-- footer -->
  <div class="abs foot-links">
    <span style="left:0">Home</span>
    <span style="left:91px">About Us</span>
    <span style="left:209px">Stories</span>
    <span style="left:313px">News</span>
    <span style="left:401px">Conatct</span>
  </div>
  <div class="abs copy">© 2020 QRSTREAMHUB. All rights reserved.</div>
  <div class="abs social" style="left:877px" aria-label="Social link"></div>
  <div class="abs social" style="left:929px" aria-label="Social link"></div>
  <div class="abs social" style="left:981px" aria-label="Social link"></div>
  <div class="abs band" style="left:0;top:3742px;width:1200px;height:8px"><span></span><span></span></div>

</div>
</body>
</html>
```